TK VESSA
transformative skincare
plant-based | clean | anti-aging
The line is for both men and women
-luxurious feeling, plant-based, all natural skincare line
This is a continuation from previous project but maybe with sans serif or serif font instead of cursive for the TK part of Vessa. (Please see logo designs from 2 years ago)
- I think TK Vessa should be smaller in size than the names of the product so people can more easily read what it says since there are a lot of products in a set.
Also, the day products will have very light cream almost white colored labels with dark green and gold fonts/accents and the night products will have dark green almost black labels with light cream and gold colored font I think.

The products are for both men and women so I don't want the labels looking too feminine? Maybe more simple or a faint leaf design in background.

-about 24 different labels for skincare jars and bottles:
Glycolic Cleanser 4oz and 8oz
Cleansing Oil 4oz and 8oz
Vitamin C Day Serum 1oz and 2oz
Stem Cell C Day Serum 1oz and 2oz
Stem Cell Day Cream 2oz and 4oz
Retinol Night Serum - Lavender 1oz and 2oz
Retinol Night Serum - Neroli 1oz and 2oz
Coconut Charcoal Scrub 2oz and 4oz
Enzyme Night Cream 2oz and 4oz
Eye Renewal Night Serum .5oz
Vitamin C Day Eye Cream .5oz
Honey Lip Balm .5oz
Enzyme Body Lotion - Vanilla Almond 8oz
Enzyme Body Lotion - Mango Lime 8oz
Enzyme Body Lotion - Lavender 8oz

Target Market(s)

ages 40-50 with some 20's and 30's sprinkled in

Industry/Entity Type

Beauty and Skincare

Font styles to use
Serif
Sans Serif
Other font styles liked:
• If you have a more unique but clean or slick font or combo of fonts in mind, please be creative!

Colors
00AB8E
00BBA5
67D7C9
C6EFE9
E9F9F6
FFF300
FFF600
FEFA6F
FFFEC7
FFFEE8

Requirements
Must have
• TK Vessa should be smaller in size than the names of the product so people can more easily read what it says since there are a lot of products in a set. day products will be light colored labels with dark green and gold fonts/accents and the night products will be on dark green labels with light cream and gold colored font
Nice to have
• Attached are original files of a logo previously designed a couple years ago but not sure I want the script TK anymore? Some sort of leaf design to go with previously made logo but want to see TK in serif or sans serif instead of script. Also attached are simple labels on the products currently and how they look as they're being sold to private clients. Wanting to put them out online for the public this year so need high end, luxurious look and feel but not generic. Thank you!
Should not have
• too busy of a design

```html
<!DOCTYPE html>
<html lang="en">
<head>
<meta charset="utf-8">
<title>TK Vessa — Vitamin C Day Eye Cream Labels</title>
<link rel="stylesheet" href="https://fonts.googleapis.com/css2?family=Cormorant+Garamond:wght@500&family=Tinos&family=Montserrat:wght@400;500&display=swap">
<style>
  :root {
    --backdrop: #8e8e8e;
    --forest: #254430;
    --cream: #f2eee5;
    --gold: #bf9a55;
    --gold-light: #f3e4bd;
    --gold-deep: #b88430;
    --leaf-night: #2c4f36;
    --leaf-day: #e2e8d3;
  }
  * { box-sizing: border-box; margin: 0; padding: 0; }
  html, body {
    width: 1200px;
    height: 1160px;
    overflow: hidden;
    background: var(--backdrop);
  }
  .label {
    position: absolute;
    left: 167px;
    width: 866px;
    height: 438px;
    overflow: hidden;
    box-shadow: 0 14px 26px rgba(0, 0, 0, 0.35);
  }
  .label--night { top: 122px; background: var(--forest); color: var(--cream); }
  .label--day { top: 599px; background: var(--cream); color: var(--forest); }

  .foliage {
    position: absolute;
    border-radius: 45%;
  }
  .foliage--left { left: 10px; top: 45px; width: 265px; height: 393px; transform: rotate(-8deg); }
  .foliage--right { left: 600px; top: 0; width: 262px; height: 392px; transform: rotate(12deg); }
  .label--night .foliage { background: radial-gradient(ellipse at center, var(--leaf-night) 0%, rgba(44, 79, 54, 0) 70%); }
  .label--day .foliage { background: radial-gradient(ellipse at center, var(--leaf-day) 0%, rgba(226, 232, 211, 0) 70%); }

  .brand {
    position: absolute;
    left: 0;
    right: 0;
    text-align: center;
    font-family: "Cormorant Garamond", serif;
    font-weight: 500;
  }
  .brand__initials { top: 22px; font-size: 82px; line-height: 1; letter-spacing: -2px; }
  .brand__name { top: 82px; font-size: 50px; line-height: 1; letter-spacing: -1px; }

  .tagline {
    position: absolute;
    left: 0;
    right: 0;
    top: 138px;
    text-align: center;
    font-family: "Montserrat", sans-serif;
    font-size: 15px;
    letter-spacing: 2.6px;
    color: var(--gold);
  }
  .claims {
    position: absolute;
    left: 320px;
    top: 163px;
    width: 227px;
    height: 19px;
    display: flex;
    align-items: center;
    justify-content: center;
    font-family: "Montserrat", sans-serif;
    font-size: 9.6px;
    letter-spacing: 1.1px;
  }
  .label--night .claims,
  .label--night .size {
    background: linear-gradient(90deg, var(--gold-deep) 0%, var(--gold-light) 40%, var(--gold-light) 55%, var(--gold-deep) 100%);
    color: var(--forest);
  }
  .label--day .claims,
  .label--day .size { background: var(--forest); color: var(--cream); }

  .product {
    position: absolute;
    left: 0;
    right: 0;
    top: 216px;
    text-align: center;
    font-family: "Tinos", serif;
    font-size: 51px;
    line-height: 50px;
    letter-spacing: -0.5px;
  }
  .label--night .product { color: var(--cream); }
  .label--day .product { color: var(--gold); }

  .size {
    position: absolute;
    left: 393px;
    top: 364px;
    width: 80px;
    height: 36px;
    display: flex;
    align-items: center;
    justify-content: center;
    font-family: "Montserrat", sans-serif;
    font-size: 20px;
    letter-spacing: 1px;
  }
</style>
</head>
<body>
  <section class="label label--night">
    <div class="foliage foliage--left" role="img" aria-label="Faint hand-drawn olive branch in the background"></div>
    <div class="foliage foliage--right" role="img" aria-label="Faint hand-drawn olive branch in the background"></div>
    <div class="brand brand__initials">TK</div>
    <div class="brand brand__name">Vessa</div>
    <p class="tagline">TRANSFORMATIVE SKINCARE</p>
    <p class="claims">PLANT-BASED | CLEAN | ANTI-AGING</p>
    <h1 class="product">VITAMIN C<br>DAY EYE CREAM</h1>
    <p class="size">5 oz</p>
  </section>

  <section class="label label--day">
    <div class="foliage foliage--left" role="img" aria-label="Faint hand-drawn olive branch in the background"></div>
    <div class="foliage foliage--right" role="img" aria-label="Faint hand-drawn olive branch in the background"></div>
    <div class="brand brand__initials">TK</div>
    <div class="brand brand__name">Vessa</div>
    <p class="tagline">TRANSFORMATIVE SKINCARE</p>
    <p class="claims">PLANT-BASED | CLEAN | ANTI-AGING</p>
    <h1 class="product">VITAMIN C<br>DAY EYE CREAM</h1>
    <p class="size">5 oz</p>
  </section>
</body>
</html>
```